Ecommerce website Home Page Design that is clean and elegant

Design a Home page for an ecommerce website. This website products and offerings will be very similar to :

breezyharborcharms.com
maplecrestbazaar.com

Target Market(s)

Consumer and small shops who can order online.

Industry/Entity Type

Retail

Number of Pages Required

1 page

Colors

Designer to choose colors to be used in the design.

Requirements
Must have
• Exact competition with similar products:
• breezyharborcharms.com
• http://www.maplecrestbazaar.com/
• Home page with featured image banner
• List of items on sale or category based items list
• atleast three banners for sale or shipping related offers.
Nice to have
• The logo has very light colors and products will have lots of colors as you can see on competition sites. So the design must consider this so that logo also stands out somewhat for branding purpose.
Should not have
• Design should not have black background

```html
<!DOCTYPE html>
<html lang="en">
<head>
<meta charset="utf-8">
<title>Partyvale — Party Supplies, Decorations &amp; Novelties</title>
<link href="https://fonts.googleapis.com/css2?family=Open+Sans:wght@400;600;700;800&family=Satisfy&family=Playfair+Display:wght@400;700&display=swap" rel="stylesheet">
<style>
:root{
  --teal:#3aa7b8;
  --teal-dark:#2a8797;
  --pink:#ef6f8e;
  --pink-soft:#f7a3b5;
  --orange:#f4a62a;
  --purple:#9a62b3;
  --lilac:#bba0d3;
  --rose:#f1a0b1;
  --mustard:#f0c04d;
  --ink:#2b2b2b;
  --text:#555;
  --muted:#8a8a8a;
  --line:#dcdcdc;
  --panel:#f1f1f1;
  --footer:#eaeaea;
  --dark:#2f2f2f;
  --white:#fff;
}
*{box-sizing:border-box;margin:0;padding:0}
html,body{width:1200px;height:3797px;overflow:hidden;background:var(--white)}
body{font-family:"Open Sans",Arial,sans-serif;color:var(--text);position:relative}
a{color:inherit;text-decoration:none}
.abs{position:absolute}
.wrap{left:73px;width:1054px}

.topbar{top:0;left:0;width:1200px;height:36px;background:var(--panel);border-bottom:1px solid var(--line)}
.topbar .welcome{position:absolute;left:73px;top:9px;font-size:13px;color:var(--text)}
.topbar .links{position:absolute;right:73px;top:0;height:36px;display:flex;align-items:center;gap:26px}
.toplink{display:flex;align-items:center;gap:6px;font-size:11px;line-height:12px;color:var(--text)}
.cartbox{width:48px;height:52px;background:var(--ink);color:var(--white);font-size:10px;font-weight:700;text-align:center;padding-top:6px;margin-top:16px}
.cartbox b{display:block;font-size:13px}

.brand{top:62px;left:73px;font-size:46px;font-weight:800;color:var(--teal);letter-spacing:-1px;display:flex;align-items:center;gap:12px}
.brand .dot{width:22px;height:22px;border-radius:50%;background:var(--pink)}
.search{top:70px;left:392px;width:330px;height:44px;border:1px solid var(--line);border-radius:22px;font-size:13px;color:var(--muted);padding:12px 20px}
.search-go{top:67px;left:698px;width:50px;height:50px;border-radius:50%;background:var(--orange);color:var(--white);font-weight:700;font-size:16px;text-align:center;line-height:50px}
.phone{top:78px;left:762px;display:flex;align-items:center;gap:8px;font-size:25px;font-weight:700;color:var(--ink)}
.message{top:82px;left:990px;font-size:18px;color:var(--pink-soft);display:flex;align-items:center;gap:6px}

.mainnav{top:142px;height:50px;background:var(--dark);display:flex}
.mainnav a{flex:1;color:var(--white);font-size:12.5px;font-weight:700;text-align:center;display:flex;align-items:center;justify-content:center;line-height:14px;border-right:1px solid #555}
.mainnav a:last-child{border-right:0}

.hero{top:197px;height:466px;overflow:hidden}
.hero-photo{position:absolute;inset:0;background:linear-gradient(180deg,#8fb9d6 0%,#b9d3e2 35%,#4f7f8a 48%,#3f94b4 58%,#8cc7d3 70%,#e6d8bf 82%,#d8c7a6 100%)}
.sale-badge{position:absolute;left:66px;top:22px;width:190px;height:130px;background:#d8242f;color:var(--white);text-align:center;padding-top:14px;border-radius:4px}
.sale-badge .big{font-size:40px;font-weight:800;line-height:40px}
.sale-badge .sm{font-size:14px;font-weight:700;line-height:16px;margin-top:6px}
.ribbon{position:absolute;left:395px;top:0;width:530px;height:110px}
.ribbon-text{position:absolute;left:500px;top:22px;width:360px;text-align:center;color:var(--white);font-size:30px;font-weight:700;line-height:32px}
.btn-teal{position:absolute;background:var(--teal);color:var(--white);font-size:15px;font-weight:700;padding:10px 28px}
.hero-arrow{position:absolute;top:210px;color:var(--white);font-size:34px}
.hero-tabs{position:absolute;left:546px;top:390px;display:flex}
.hero-tab{width:170px;height:76px;padding:18px 20px;background:rgba(255,255,255,.85);font-size:15px;font-weight:700;color:var(--ink);line-height:17px}
.hero-tab small{display:block;font-weight:400;font-size:12px;color:var(--text)}
.hero-tab.active{background:var(--teal-dark);color:var(--white)}
.hero-tab.active small{color:var(--white)}

.members{top:668px;height:56px;border:1px solid var(--line);display:flex;align-items:center;gap:14px;font-size:12px}
.members .area{background:var(--teal);color:var(--white);font-weight:700;font-size:15px;height:100%;padding:0 24px;display:flex;align-items:center}
.pill{background:var(--pink-soft);color:var(--white);font-weight:700;padding:6px 12px;font-size:12px}
.members .plans{font-weight:800;color:var(--ink);font-size:14px;line-height:15px;text-align:center}
.members .perk{background:var(--pink-soft);color:var(--white);padding:6px 12px;width:200px;line-height:14px}
.members .view{color:var(--teal);font-weight:700}

.shipping{top:760px;height:113px;display:flex;justify-content:center;gap:44px}
.ship{width:260px;text-align:center;position:relative;padding-top:14px}
.ship::before{content:"";position:absolute;top:0;left:50%;width:80px;height:4px;margin-left:-40px;background:var(--c)}
.ship h3{font-size:17px;font-weight:700;color:var(--ink);line-height:24px}
.ship h3 span{color:var(--c)}
.ship .code{display:inline-block;margin-top:6px;background:var(--panel);border:1px solid var(--line);padding:4px 16px;font-size:12px}

.tiles{top:924px;height:258px;display:flex;gap:6px}
.tile{flex:1;position:relative}
.tile .ph{position:absolute;inset:0}
.tile h4{position:absolute;left:18px;top:14px;font-size:28px;font-weight:400;color:var(--white);line-height:30px}
.shop-tag{position:absolute;background:#111;color:var(--white);font-size:13px;font-weight:700;padding:7px 14px}
.tile .shop-tag{right:0;bottom:0}

.wedding{top:1220px;height:256px}
.wedding .ph{position:absolute;inset:0;background:linear-gradient(90deg,#7d6a52 0%,#b9a58a 30%,#a89a88 60%,#c8bcae 100%)}
.wedding .title{position:absolute;left:350px;top:0;font-family:"Playfair Display",serif;color:var(--white);font-size:66px;line-height:70px}
.wedding .sub{position:absolute;left:352px;top:150px;color:var(--white);font-size:21px}
.wedding .pct{position:absolute;left:420px;top:190px;color:var(--white);font-size:18px;line-height:20px;text-align:center}
.wedding .pct b{font-family:"Playfair Display",serif;font-size:40px;display:block;line-height:42px}
.wedding .items{position:absolute;left:855px;top:44px;color:var(--white);text-align:center;font-size:16px;line-height:18px}
.wedding .items b{font-family:"Playfair Display",serif;font-size:42px;display:block;line-height:46px;font-weight:400}
.wedding .shop-tag{left:875px;top:150px}

.sec-title{height:40px;display:flex;align-items:center;gap:20px}
.sec-title::before,.sec-title::after{content:"";flex:1;height:14px;background:var(--panel)}
.sec-title h2{font-family:"Satisfy",cursive;font-weight:400;font-size:30px;color:var(--ink)}

.cats{top:1600px;display:grid;grid-template-columns:repeat(4,243px);column-gap:28px;row-gap:30px}
.cat .ph{height:193px}
.cat p{text-align:center;font-size:14px;color:var(--ink);margin-top:20px;line-height:18px}
.cat small{display:block;text-align:center;font-size:11px;color:var(--teal)}
.divider{height:4px;background:var(--ink)}
.view-more{position:absolute;left:50%;top:-16px;margin-left:-55px;width:110px;height:34px;background:#111;color:var(--white);font-size:13px;font-weight:700;text-align:center;line-height:34px;outline:8px solid var(--white)}

.circles{top:2253px;display:flex;gap:28px}
.circle{width:243px;height:243px;border-radius:50%;background:var(--c);position:relative;text-align:center;color:var(--white)}
.circle svg{position:absolute;left:96px;top:52px}
.circle h3{position:absolute;top:125px;width:100%;font-size:26px;font-weight:400;line-height:28px}
.circle .shop-tag{left:80px;top:195px;border-radius:14px;padding:4px 16px;font-size:12px}

.products{top:2628px;display:grid;grid-template-columns:repeat(4,243px);column-gap:28px}
.prod .ph{height:218px}
.prod .name{margin-top:20px;font-size:13px;color:var(--teal);line-height:18px;height:38px}
.prod .price{font-size:16px;color:var(--ink);margin-top:8px;font-weight:600}
.prod .cart{display:inline-block;margin-top:12px;background:var(--lilac);color:var(--white);font-size:12px;font-weight:700;padding:6px 14px}

.semi{top:3107px;height:260px;background:var(--pink);overflow:hidden}
.semi .art{position:absolute;left:150px;top:30px;width:460px;height:200px;background:linear-gradient(90deg,#f6d3dc,#f7d64a 55%,#2f8fae);border-radius:8px}
.semi .blob{position:absolute;left:700px;top:26px;width:340px;height:208px;background:var(--purple);border-radius:46% 54% 40% 60%/50% 40% 60% 50%}
.semi .stock{position:absolute;left:0;width:100%;top:34px;text-align:center;color:var(--white);font-size:44px;font-weight:700;line-height:46px}
.semi .trend{position:absolute;left:0;width:100%;top:86px;text-align:center;color:var(--white);font-size:16px;line-height:18px}
.semi .shop-tag{left:130px;top:138px}

.footer{top:3431px;left:0;width:1200px;height:280px;background:var(--footer)}
.fcols{position:absolute;left:73px;top:40px;display:flex;gap:30px}
.fcol{width:156px;font-size:12.5px;line-height:25px}
.fcol.wide{width:210px}
.fcol h5{font-size:13px;font-weight:800;color:var(--ink);margin-bottom:4px}
.news{position:absolute;left:715px;top:30px;width:412px;height:210px;background:var(--white);border:1px solid var(--line);padding:18px}
.news h5{font-size:15px;font-weight:800;color:var(--ink)}
.news p{font-size:12.5px;margin-top:4px}
.news .field{display:flex;margin-top:14px}
.news .field span{flex:1;border:1px solid var(--line);height:38px;font-size:12.5px;padding:10px 12px;color:var(--muted)}
.news .field b{background:var(--ink);color:var(--white);width:72px;text-align:center;line-height:38px;font-size:15px}
.social{display:flex;gap:10px;margin-top:12px}
.social i{width:36px;height:36px;border-radius:50%;background:#8a8a8a;display:block}
.fmsg{position:absolute;left:500px;top:224px;font-size:15px;color:var(--muted);display:flex;gap:6px;align-items:center}
.bottombar{top:3712px;left:0;width:1200px;height:85px;background:var(--dark);color:#cfcfcf;font-size:13px}
.bottombar .copy{position:absolute;left:73px;top:33px}
.bottombar .mark{position:absolute;left:433px;width:334px;top:16px;text-align:center;color:var(--teal);font-size:40px;font-weight:800;letter-spacing:-1px}
.bottombar .accept{position:absolute;right:73px;top:26px;display:flex;gap:8px;align-items:center;font-weight:700;color:var(--white)}
.bottombar .accept i{width:50px;height:32px;background:var(--white);border-radius:3px;display:block}
</style>
</head>
<body>

<div class="abs topbar">
  <span class="welcome">Welcome to Partyvale</span>
  <div class="links">
    <span class="toplink"><svg width="16" height="16" viewBox="0 0 16 16"><circle cx="8" cy="5" r="3.5" fill="none" stroke="#777" stroke-width="1.5"/><path d="M1.5 15c1-4 12-4 13 0" fill="none" stroke="#777" stroke-width="1.5"/></svg>Hello<br>Log In</span>
    <span class="toplink"><svg width="16" height="16" viewBox="0 0 16 16"><path d="M8 14 2 8a3.2 3.2 0 0 1 6-4 3.2 3.2 0 0 1 6 4z" fill="none" stroke="#777" stroke-width="1.5"/></svg>Wish<br>List</span>
    <span class="toplink"><svg width="18" height="14" viewBox="0 0 18 14"><path d="M1 2h10v8H1zM11 5h4l2 3v2h-6" fill="none" stroke="#777" stroke-width="1.5"/><circle cx="4" cy="12" r="1.5" fill="#777"/><circle cx="14" cy="12" r="1.5" fill="#777"/></svg>Track<br>Orders</span>
    <span class="cartbox"><b>0</b>CART</span>
  </div>
</div>

<div class="abs brand"><span>Partyvale</span><span class="dot"></span></div>
<div class="abs search">Enter Keyword or Item #</div>
<div class="abs search-go">Go</div>
<div class="abs phone"><svg width="24" height="24" viewBox="0 0 24 24"><circle cx="12" cy="12" r="11" fill="none" stroke="#3aa7b8" stroke-width="2"/><path d="M8 6l2 0 1 3-1.5 1a7 7 0 0 0 4 4L15 12.5l3 1v2a2 2 0 0 1-2 2A10 10 0 0 1 6.5 8 2 2 0 0 1 8 6z" fill="#3aa7b8"/></svg>1-800-555-0142</div>
<div class="abs message"><svg width="20" height="18" viewBox="0 0 20 18"><path d="M1 1h18v12H7l-4 4v-4H1z" fill="none" stroke="#f7a3b5" stroke-width="1.6"/></svg>Message Us</div>

<nav class="abs wrap mainnav">
  <a href="#">Luau</a><a href="#">Party<br>Themes</a><a href="#">Holidays &amp;<br>Occasions</a><a href="#">Decorations &amp;<br>Supplies</a><a href="#">Glow<br>Products</a><a href="#">LED<br>Products</a><a href="#">Party<br>Wearables</a><a href="#">Party<br>Ideas</a>
</nav>

<section class="abs wrap hero">
  <div class="hero-photo" role="img" aria-label="Hula dancer in a grass skirt holding red flowers on a tropical beach with green mountains and sea"></div>
  <div class="sale-badge"><div class="big">LUAU<br>SALE</div><div class="sm">UP TO<br>50% OFF</div></div>
  <svg class="ribbon" viewBox="0 0 530 110" aria-hidden="true"><path d="M0 40 Q60 20 120 30 L530 0 L500 55 L530 105 L110 90 Q60 85 0 100 Z" fill="#f3a0b6"/></svg>
  <div class="ribbon-text">Let's Luau<br>All Summer Long!</div>
  <a class="btn-teal" style="left:600px;top:104px" href="#">Shop Now</a>
  <span class="hero-arrow" style="left:10px">&#8592;</span>
  <span class="hero-arrow" style="right:10px">&#8594;</span>
  <div class="hero-tabs">
    <div class="hero-tab">SUMMER<small>Shop Now</small></div>
    <div class="hero-tab active">LUAU<small>Shop Now</small></div>
    <div class="hero-tab">WEDDING<small>Shop Now</small></div>
  </div>
</section>

<div class="abs wrap members">
  <span class="area">Members Area</span>
  <span class="pill">LOG IN</span>
  <span class="plans">MEMBERSHIP<br>PLANS</span>
  <span class="perk">Get preferred discount &amp; bonus points with every</span>
  <span class="perk" style="width:150px">Priority Shipping for Members</span>
  <span class="view">View Membership Plans &rsaquo;</span>
  <span class="pill">SIGNUP</span>
</div>

<div class="abs wrap shipping">
  <div class="ship" style="--c:var(--teal)"><h3>FREE Shipping &amp; <span>$10 Off</span><br>Orders $99+</h3><span class="code">use code:SHIP99</span></div>
  <div class="ship" style="--c:var(--orange)"><h3>FREE Shipping &amp; <span>$20 Off</span><br>Orders $199+</h3><span class="code">use code:SHIP199</span></div>
  <div class="ship" style="--c:var(--pink)"><h3>FREE Shipping &amp; <span>$30 Off</span><br>Orders $299+</h3><span class="code">use code:SHIP299</span></div>
</div>

<div class="abs wrap tiles">
  <div class="tile"><div class="ph" role="img" aria-label="Rustic wedding table with lantern, flowers and wooden love letters" style="background:linear-gradient(135deg,#6b4b36,#b08d6e 60%,#e6dccd)"></div><h4>Wedding<br>Decorations</h4><span class="shop-tag">Shop Now</span></div>
  <div class="tile"><div class="ph" role="img" aria-label="Bright glowing necklaces in many colours on black" style="background:radial-gradient(circle at 55% 55%,#3a7a3a,#1d3350 45%,#050505 80%)"></div><h4>Glow<br>Necklaces</h4><span class="shop-tag">Shop Now</span></div>
  <div class="tile"><div class="ph" role="img" aria-label="Group of friends at a festive theme party" style="background:linear-gradient(135deg,#6a1c1c,#b23a2e 50%,#d98a5a)"></div><h4>Theme<br>Parties</h4><span class="shop-tag">Shop Now</span></div>
</div>

<section class="abs wrap wedding">
  <div class="ph" role="img" aria-label="Wedding lantern with flowers and a bride and groom cake topper"></div>
  <div class="title">Wedding<br>Sale</div>
  <div class="sub">Celebrate Your Big Day</div>
  <div class="pct">Up To<b>60% OFF</b></div>
  <div class="items"><b>100s</b>Of Items - Just<br>Added!</div>
  <span class="shop-tag">Shop Now</span>
</section>

<div class="abs wrap sec-title" style="top:1537px"><h2>Shop Top Categories</h2></div>

<div class="abs wrap cats">
  <div class="cat"><div class="ph" role="img" aria-label="Colourful party balloons and confetti" style="background:linear-gradient(135deg,#3b5bb5,#e0b23a 50%,#c7342b)"></div><p>Party &amp; Birthday Balloons</p><small>Shop Now</small></div>
  <div class="cat"><div class="ph" role="img" aria-label="Runner wearing a glowing LED armband" style="background:radial-gradient(circle,#5a2a6a,#111 70%)"></div><p>LED Jewelry</p><small>Shop Now</small></div>
  <div class="cat"><div class="ph" role="img" aria-label="Champagne glasses wrapped in lace fabric" style="background:linear-gradient(135deg,#c9a57a,#efe3cf)"></div><p>Decorating Fabric</p><small>Shop Now</small></div>
  <div class="cat"><div class="ph" role="img" aria-label="Box of pink and purple flowers" style="background:linear-gradient(135deg,#9b8aa6,#e6c4d0)"></div><p>Anniversary Decorations</p><small>Shop Now</small></div>
  <div class="cat"><div class="ph" role="img" aria-label="Table setting with plate and rosemary" style="background:linear-gradient(135deg,#5b4a3a,#c9b79a)"></div><p>Tableware</p><small>Shop Now</small></div>
  <div class="cat"><div class="ph" role="img" aria-label="Party hats and noise makers" style="background:linear-gradient(135deg,#cfe6ef,#f3d98a)"></div><p>Noise Makers</p><small>Shop Now</small></div>
  <div class="cat"><div class="ph" role="img" aria-label="Friends posing with photo booth props under bunting" style="background:linear-gradient(135deg,#d9d2c2,#b4453a 60%,#5a7ca8)"></div><p>Photo Booth Supplies</p><small>Shop Now</small></div>
  <div class="cat"><div class="ph" role="img" aria-label="Rows of glowing drink cups" style="background:linear-gradient(180deg,#0a0a14,#2b3a7a 70%,#0a0a14)"></div><p>Glow Drinkware</p><small>Shop Now</small></div>
</div>

<div class="abs wrap divider" style="top:2165px"><a class="view-more" href="#">View More</a></div>

<div class="abs wrap circles">
  <div class="circle" style="--c:var(--teal)"><svg width="50" height="50" viewBox="0 0 50 50"><g fill="none" stroke="#fff" stroke-width="2.5"><rect x="6" y="26" width="38" height="18"/><rect x="10" y="16" width="30" height="10"/><path d="M16 16V8M25 16V8M34 16V8"/></g></svg><h3>Milestone<br>Birthdays</h3><span class="shop-tag">Shop Now</span></div>
  <div class="circle" style="--c:var(--lilac)"><svg width="50" height="50" viewBox="0 0 50 50"><g fill="none" stroke="#fff" stroke-width="2.5"><circle cx="16" cy="12" r="7"/><circle cx="32" cy="12" r="7"/><rect x="8" y="22" width="28" height="18"/><path d="M36 28l10-5v16l-10-5"/></g></svg><h3>Hollywood<br>Parties</h3><span class="shop-tag">Shop Now</span></div>
  <div class="circle" style="--c:var(--rose)"><svg width="50" height="50" viewBox="0 0 50 50"><g fill="none" stroke="#fff" stroke-width="2.5"><rect x="8" y="22" width="34" height="22"/><rect x="5" y="15" width="40" height="7"/><path d="M25 15v29M25 15c-4-9-13-6-8 0M25 15c4-9 13-6 8 0"/></g></svg><h3>Dancefloor<br>Giveaways</h3><span class="shop-tag">Shop Now</span></div>
  <div class="circle" style="--c:var(--mustard)"><svg width="50" height="50" viewBox="0 0 50 50"><path d="M25 3l5 6 8-2 1 8 7 4-4 7 4 7-7 4-1 8-8-2-5 6-5-6-8 2-1-8-7-4 4-7-4-7 7-4 1-8 8 2z" fill="none" stroke="#fff" stroke-width="2.5"/></svg><h3>New<br>Products</h3><span class="shop-tag">Shop Now</span></div>
</div>

<div class="abs wrap sec-title" style="top:2558px"><h2>Featured Product</h2></div>

<div class="abs wrap products">
  <div class="prod"><div class="ph" role="img" aria-label="Green glowing ice cube in a drink" style="background:radial-gradient(circle,#6fe07a,#1a5a22 50%,#050505 85%)"></div><p class="name">Neon Green LED and Light - Up Ice Cube - 12 pack</p><p class="price">$22.50</p><span class="cart">ADD TO CART</span></div>
  <div class="prod"><div class="ph" role="img" aria-label="Woman wearing a star-spangled top hat" style="background:linear-gradient(135deg,#1f2a6a,#c7333a 55%,#f2f2f2)"></div><p class="name">LED Uncle Sam Hat</p><p class="price">$2.95</p><span class="cart">ADD TO CART</span></div>
  <div class="prod"><div class="ph" role="img" aria-label="Woman waving a light-up flag foam stick" style="background:linear-gradient(135deg,#0c0c1c,#8a1a2a 60%,#1c2a6a)"></div><p class="name">LED American Flag Foam Light Stick</p><p class="price">$2.80</p><span class="cart">ADD TO CART</span></div>
  <div class="prod"><div class="ph" role="img" aria-label="Multicolour flower lei" style="background:radial-gradient(circle,#ffffff 30%,#f0a030 45%,#e04a8a 60%,#5ac0e0 75%,#ffffff 90%)"></div><p class="name">Neon Green LED and Light - Up Ice Cube - 12 pack</p><p class="price">$16.00</p><span class="cart">ADD TO CART</span></div>
</div>

<div class="abs wrap divider" style="top:3019px"><a class="view-more" href="#">View More</a></div>

<section class="abs wrap semi">
  <div class="art" role="img" aria-label="Semi-Annual Sale hand lettering with paint splashes"></div>
  <div class="blob">
    <div class="stock">Stock Up!</div>
    <div class="trend">ON TOP<br>TRENDING ITEMS</div>
    <span class="shop-tag">Shop Now</span>
  </div>
</section>

<footer class="abs footer">
  <div class="fcols">
    <div class="fcol"><h5>CUSTOMER SERVICE</h5>Contact Us<br>Help &amp; FAQ<br>Order Tracking<br>Return Policy<br>Shipping Information<br>Shopping Cart<br>International Orders</div>
    <div class="fcol wide"><h5>ABOUT US</h5>Company Information<br>Employment<br>Affiliate Program<br>110% Lowest Price Guarantee<br>100% Happiness Guarantee<br>Our Family Of Brands<br>Company News</div>
    <div class="fcol wide"><h5>SAFE &amp; SECURE SHOPPING</h5>Security/Privacy<br>Terms &amp; Conditions<br>Your California Privacy Rights<br>Site Map<br>Safety News</div>
  </div>
  <div class="fmsg"><svg width="20" height="18" viewBox="0 0 20 18"><path d="M1 1h18v12H7l-4 4v-4H1z" fill="none" stroke="#8a8a8a" stroke-width="1.6"/></svg>Message Us</div>
  <div class="news">
    <h5>JOIN OUR NEWSLETTER</h5>
    <p>Discover exclusive offers, products preview and much more</p>
    <div class="field"><span>Enter your email address</span><b>JOIN</b></div>
    <h5 style="margin-top:16px;font-size:13px">STAY CONNECTED WITH PARTYVALE!</h5>
    <div class="social"><i></i><i></i><i></i><i></i><i></i><i></i></div>
  </div>
</footer>

<div class="abs bottombar">
  <span class="copy">&copy; 2017 Partyvale. All Rights Reserved.</span>
  <span class="mark">Partyvale</span>
  <div class="accept">WE ACCEPT <i></i><i></i><i></i><i></i><i></i></div>
</div>

</body>
</html>
```